Business Card Design for Technology Company

New business card design needed for technology company director.
Ideally, the design will fit the style and nature of the industry. We are a supplier of quality products and services, and we hope the design will give customers and suppliers this impression.

Target Market(s)

3D Printing Industry

Industry/Entity Type

Technology Equipment

Contact Information for Business Card

Name: Henry Vo
Title: Director
Company address: Factory K4, 7B Lorimer Road, Kelsworth Eastvale Australia 3975
Telephone: +61-7-2614 4613
Email: henry.vo@ferrolabs.com.au
Website: www.ferrolabs.com.au

Requirements
Must have
• All information in business card details
• Company logo
• '3D Printers and 3D Print Filaments' at proper place
Nice to have
• Style to fit the industry
• Colour to fit logo

```html
<!DOCTYPE html>
<html lang="en">
<head>
<meta charset="utf-8">
<title>Ferro Labs – Business Card</title>
<link href="https://fonts.googleapis.com/css2?family=Open+Sans:ital,wght@0,300;0,400;0,600;1,700&display=swap" rel="stylesheet">
<style>
  :root {
    --bg: #4a413c;
    --card: #1c1e21;
    --text: #f2f2f2;
    --muted: #c9ccd0;
    --blue: #1f6fb8;
    --orange: #f08a1c;
    --rule: #d6d6d6;
  }
  html, body {
    margin: 0;
    width: 1200px;
    height: 864px;
    overflow: hidden;
    background: var(--bg);
    font-family: "Open Sans", Arial, sans-serif;
  }
  .stage {
    width: 1200px;
    height: 864px;
    display: flex;
    flex-direction: column;
    align-items: center;
    justify-content: center;
    gap: 36px;
  }
  .card {
    position: relative;
    width: 620px;
    height: 378px;
    background: var(--card);
    box-shadow: 0 10px 24px rgba(0,0,0,.45);
    color: var(--text);
    box-sizing: border-box;
  }
  .brand {
    display: flex;
    align-items: center;
    gap: 14px;
  }
  .brand-square {
    width: 34px;
    height: 34px;
    background: var(--orange);
  }
  .brand-name {
    font-weight: 600;
    font-size: 30px;
    letter-spacing: 6px;
    color: var(--muted);
    text-transform: uppercase;
  }
  .card-front {
    display: flex;
    flex-direction: column;
    align-items: center;
    justify-content: center;
    gap: 34px;
  }
  .tagline {
    margin: 0;
    font-weight: 300;
    font-size: 17px;
    letter-spacing: 4px;
    color: var(--text);
  }
  .card-back .brand {
    position: absolute;
    top: 52px;
    right: 44px;
  }
  .card-back .brand-name { color: var(--text); font-size: 28px; }
  .person {
    position: absolute;
    left: 44px;
    top: 118px;
  }
  .person-name {
    margin: 0;
    font-weight: 700;
    font-style: italic;
    font-size: 22px;
    color: var(--blue);
    text-transform: uppercase;
    line-height: 1.1;
  }
  .person-title {
    margin: 0;
    font-size: 16px;
    color: var(--orange);
    text-transform: uppercase;
  }
  .divider {
    position: absolute;
    left: 44px;
    right: 44px;
    top: 196px;
    height: 1px;
    background: var(--rule);
  }
  .contacts {
    position: absolute;
    left: 44px;
    top: 212px;
    margin: 0;
    padding: 0;
    list-style: none;
    font-size: 15px;
    line-height: 1.55;
  }
  .contacts li { display: flex; align-items: center; gap: 9px; }
  .contacts svg { width: 13px; height: 13px; fill: var(--blue); flex: none; }
  .address {
    position: absolute;
    right: 44px;
    bottom: 40px;
    margin: 0;
    text-align: right;
    font-style: normal;
    font-size: 16px;
    line-height: 1.4;
  }
</style>
</head>
<body>
<main class="stage">
  <section class="card card-front">
    <div class="brand">
      <span class="brand-square"></span>
      <span class="brand-name">Ferro Labs</span>
    </div>
    <p class="tagline">3D Printers and 3D Print Filaments</p>
  </section>

  <section class="card card-back">
    <div class="brand">
      <span class="brand-square"></span>
      <span class="brand-name">Ferro Labs</span>
    </div>
    <div class="person">
      <h1 class="person-name">Henry Vo</h1>
      <p class="person-title">Director</p>
    </div>
    <div class="divider"></div>
    <ul class="contacts">
      <li>
        <svg viewBox="0 0 16 16" aria-hidden="true"><path d="M3 1h3l1.5 4-2 1.3a9 9 0 0 0 4.2 4.2L11 8.5l4 1.5v3a2 2 0 0 1-2 2A13 13 0 0 1 1 3a2 2 0 0 1 2-2z"/></svg>
        +61-7-2614 4613
      </li>
      <li>
        <svg viewBox="0 0 16 16" aria-hidden="true"><path d="M1 3h14v10H1z M1 3l7 6 7-6" stroke="#1c1e21" stroke-width="1.2"/></svg>
        henry.vo@ferrolabs.com.au
      </li>
      <li>
        <svg viewBox="0 0 16 16" aria-hidden="true"><circle cx="8" cy="8" r="7"/><path d="M1 8h14M8 1c3 3 3 11 0 14M8 1c-3 3-3 11 0 14" stroke="#1c1e21" stroke-width="1" fill="none"/></svg>
        www.ferrolabs.com.au
      </li>
    </ul>
    <address class="address">
      Factory K4, 7B Lorimer Road,<br>
      Kelsworth Eastvale<br>
      Australia 3975
    </address>
  </section>
</main>
</body>
</html>
```